The Christian Teacher Life-Cycle

Look at the Lifecyle of the Christian School.
Look at the BLT logo.
I am looking for a Christian Teacher Lifecycle that represents the slides in the PP upload.
Our website is bramblewoodlearningtrust.org.
The design should include a summary design showing all four stages, and then four slides representing each of the stages as subsets of the summary design.
When a teacher is going through the Lifecycle, they are going on their Professional Learning Journey that takes 40 years to unfold.
All five should include a copyright 2026 BLT on them.

```html
<!DOCTYPE html>
<html lang="en">
<head>
<meta charset="utf-8">
<title>Christian Teacher Lifecycle – BLT</title>
<link href="https://fonts.googleapis.com/css2?family=Playfair+Display:wght@400&family=Montserrat:wght@400;500&display=swap" rel="stylesheet">
<style>
  :root{
    --page:#ffffff;
    --sky-top:#dbe8f6;
    --sky-mid:#eef4fb;
    --ink:#1b2a4a;
    --title:#1f2d55;
    --badge:#1f6fc0;
    --bullet:#1f6fc0;
    --card:rgba(232,238,247,.85);
    --card-edge:rgba(255,255,255,.9);
    --leaf-a:#1a3fa0;
    --leaf-b:#5b8ee0;
    --tree:#c9d6e8;
    --muted:#7a879e;
  }
  *{box-sizing:border-box;margin:0;padding:0}
  html,body{width:1200px;height:575px;overflow:hidden;background:var(--page)}
  body{position:relative;font-family:"Montserrat",sans-serif;color:var(--ink)}

  .slide{position:absolute;width:388px;height:274px;overflow:hidden;
    background:linear-gradient(160deg,var(--sky-top) 0%,var(--sky-mid) 45%,#f7fafd 100%)}
  .slide--overview{left:10px;top:9px}
  .slide--step1{left:406px;top:9px}
  .slide--step2{left:802px;top:9px}
  .slide--step3a{left:10px;top:291px}
  .slide--step3b{left:406px;top:291px}
  .slide--step4{left:802px;top:291px}

  .scenery{position:absolute;left:0;top:0;width:388px;height:274px}
  .tree{position:absolute;border-radius:45% 45% 10% 10%;
    background:radial-gradient(ellipse at 50% 40%,var(--tree),rgba(201,214,232,0) 70%)}
  .tree--left{left:0;top:118px;width:40px;height:62px}
  .tree--right{right:8px;top:132px;width:44px;height:56px}
  .leaves{position:absolute;left:0;top:204px;width:70px;height:70px;border-radius:40% 60% 0 0;
    background:linear-gradient(35deg,var(--leaf-a) 0%,var(--leaf-b) 55%,rgba(91,142,224,0) 90%);opacity:.8}

  .slide-title{position:absolute;left:78px;top:20px;font-family:"Playfair Display",serif;
    font-weight:400;font-size:21px;line-height:1;color:var(--title);white-space:nowrap}
  .slide--overview .slide-title{left:89px;top:19px;font-size:17px}

  .stage-card{position:absolute;top:61px;width:69px;height:140px;border-radius:7px 7px 0 0;
    background:linear-gradient(180deg,var(--card),rgba(232,238,247,.2));
    border:1px solid var(--card-edge);border-bottom:none;text-align:center}
  .stage-badge{position:absolute;left:50%;top:-8px;transform:translateX(-50%);
    width:17px;height:17px;border-radius:50%;background:var(--badge);color:#fff;
    border:1px solid #fff;font-size:6.5px;font-weight:500;line-height:15px}
  .stage-name{position:absolute;left:8px;right:8px;top:18px;font-size:5.4px;line-height:1.25}
  .stage-name--lead{left:4px;right:4px;font-size:6.4px;font-weight:500;top:16px}
  .stage-name--wide{left:4px;right:4px}
  .stage-rule{position:absolute;left:25px;right:25px;top:57px;height:1px;background:#8fb0dc}
  .stage-years{position:absolute;left:0;right:0;top:66px;font-size:5.3px}
  .doves{position:absolute;left:50%;transform:translateX(-50%);top:82px;width:42px;height:36px;
    border-radius:50%;background:radial-gradient(ellipse,rgba(31,111,192,.75),rgba(31,111,192,.25) 55%,rgba(31,111,192,0) 72%)}

  .detail-card{left:37px}
  .detail-card .stage-name{left:4px;right:4px;font-size:6.4px;line-height:1.2;
    display:flex;align-items:center;justify-content:center;height:80px;top:10px}

  .points{position:absolute;left:126px;right:14px;list-style:none;font-size:6.6px;font-weight:500;line-height:1.3}
  .points li{position:relative;padding-left:8px}
  .points li::before{content:"";position:absolute;left:0;top:2.6px;width:3px;height:3px;background:var(--bullet)}
  .points--roomy{top:73px}
  .points--roomy li{margin-bottom:8px}
  .points--snug{top:74px;font-weight:400}
  .points--snug li{margin-bottom:5.6px}
  .slide--step2 .points{top:76px}
  .slide--step4 .points{top:67px}
  .slide--step4 .points li:first-child{margin-bottom:4px}

  .brand-name{position:absolute;left:166px;top:226px;width:70px;text-align:center;
    font-family:"Montserrat",sans-serif;font-weight:500;font-size:21px;line-height:1;color:var(--title);letter-spacing:1px}
  .copyright{position:absolute;left:327px;top:261px;font-size:3.8px;color:var(--muted);white-space:nowrap}
</style>
</head>
<body>

<svg width="0" height="0" style="position:absolute" aria-hidden="true">
  <defs>
    <linearGradient id="hillBack" x1="0" y1="0" x2="1" y2="0">
      <stop offset="0" stop-color="#a9bfe2"/><stop offset=".5" stop-color="#dfe8f5"/><stop offset="1" stop-color="#9fb5dc"/>
    </linearGradient>
    <linearGradient id="hillFront" x1="0" y1="0" x2="0" y2="1">
      <stop offset="0" stop-color="#e8eff8"/><stop offset="1" stop-color="#ffffff"/>
    </linearGradient>
    <symbol id="hills" viewBox="0 0 388 274">
      <path d="M0 176 C60 168 95 200 150 204 C215 208 260 196 300 195 C340 194 365 186 388 178 L388 274 L0 274Z" fill="url(#hillBack)" opacity=".75"/>
      <path d="M0 196 C70 190 110 214 180 214 C250 214 300 206 388 204 L388 274 L0 274Z" fill="url(#hillFront)"/>
    </symbol>
  </defs>
</svg>

<section class="slide slide--overview">
  <svg class="scenery" aria-hidden="true"><use href="#hills"/></svg>
  <div class="tree tree--left" role="img" aria-label="Faint tree silhouette"></div>
  <div class="tree tree--right" role="img" aria-label="Faint tree silhouette"></div>
  <h1 class="slide-title">Christian Teacher Lifecycle</h1>

  <div class="stage-card" style="left:37px">
    <div class="stage-badge">01</div>
    <p class="stage-name stage-name--lead">The focus<br>is on “I”</p>
    <div class="stage-rule"></div>
    <p class="stage-years">0-5 years</p>
    <div class="doves" role="img" aria-label="One blue dove in flight"></div>
  </div>
  <div class="stage-card" style="left:115px">
    <div class="stage-badge">02</div>
    <p class="stage-name">Becoming part of the Christian Professional Learning Community</p>
    <div class="stage-rule"></div>
    <p class="stage-years">5-10 years</p>
    <div class="doves" role="img" aria-label="One blue dove with two grey doves"></div>
  </div>
  <div class="stage-card" style="left:194px">
    <div class="stage-badge">03</div>
    <p class="stage-name stage-name--wide">Learning leadership within the faculty culture / CPLC</p>
    <div class="stage-rule"></div>
    <p class="stage-years">10-30 years</p>
    <div class="doves" role="img" aria-label="One blue dove with two grey doves"></div>
  </div>
  <div class="stage-card" style="left:272px">
    <div class="stage-badge">04</div>
    <p class="stage-name stage-name--wide">So good, I am<br>“invisible”; I have<br>let go of control<br>and share it with<br>my children/teens</p>
    <div class="stage-rule"></div>
    <p class="stage-years">30-40 years</p>
    <div class="doves" role="img" aria-label="Three blue doves in flight"></div>
  </div>

  <div class="leaves" role="img" aria-label="Blue olive branch leaves"></div>
  <p class="brand-name">BLT</p>
  <p class="copyright">Copyright© 2026 BLT</p>
</section>

<section class="slide slide--step1">
  <svg class="scenery" aria-hidden="true"><use href="#hills"/></svg>
  <div class="tree tree--left" role="img" aria-label="Faint tree silhouette"></div>
  <div class="tree tree--right" role="img" aria-label="Faint tree silhouette"></div>
  <h2 class="slide-title">Step 1 : Learning Journey</h2>
  <div class="stage-card detail-card">
    <div class="stage-badge">01</div>
    <p class="stage-name">The focus<br>is on “I”</p>
    <div class="doves" role="img" aria-label="One blue dove in flight"></div>
  </div>
  <ul class="points points--roomy">
    <li>Fundamental skills dominate<br>such as classroom management</li>
    <li>Curriculum is where I spend my time</li>
    <li>I am a sponge rather than a contributor</li>
    <li>I see myself as a learner</li>
    <li>I reflect on my practice</li>
  </ul>
  <div class="leaves" role="img" aria-label="Blue olive branch leaves"></div>
  <p class="brand-name">BLT</p>
  <p class="copyright">Copyright© 2026 BLT</p>
</section>

<section class="slide slide--step2">
  <svg class="scenery" aria-hidden="true"><use href="#hills"/></svg>
  <div class="tree tree--left" role="img" aria-label="Faint tree silhouette"></div>
  <div class="tree tree--right" role="img" aria-label="Faint tree silhouette"></div>
  <h2 class="slide-title">Step 2 : Learning Journey</h2>
  <div class="stage-card detail-card">
    <div class="stage-badge">02</div>
    <p class="stage-name">Becoming part of the Christian Professional Learning Community</p>
    <div class="doves" role="img" aria-label="One blue dove with two grey doves"></div>
  </div>
  <ul class="points points--roomy">
    <li>My Christian Professional Learning Community is<br>important to me as a place where I give and take</li>
    <li>I recognize that “we” is more powerful for the child than “I”</li>
    <li>I know my curriculum - I am more focused on how, on pedagogy</li>
    <li>I assess relevant and effective assessment tools</li>
    <li>I reflect on my practice</li>
  </ul>
  <div class="leaves" role="img" aria-label="Blue olive branch leaves"></div>
  <p class="brand-name">BLT</p>
  <p class="copyright">Copyright© 2026 BLT</p>
</section>

<section class="slide slide--step3a">
  <svg class="scenery" aria-hidden="true"><use href="#hills"/></svg>
  <div class="tree tree--left" role="img" aria-label="Faint tree silhouette"></div>
  <div class="tree tree--right" role="img" aria-label="Faint tree silhouette"></div>
  <h2 class="slide-title">Step 3A : Learning Journey</h2>
  <div class="stage-card detail-card">
    <div class="stage-badge">03</div>
    <p class="stage-name">The focus<br>is on “I”</p>
    <div class="doves" role="img" aria-label="One blue dove with two grey doves"></div>
  </div>
  <ul class="points points--snug">
    <li>I lead in my Christian Professional Learning Community</li>
    <li>Ensuring my colleagues continue to grow is critical to me</li>
    <li>Together, we are humble in understanding where we still need to go</li>
    <li>My colleagues see me as an important resource</li>
    <li>I am a master of growth</li>
    <li>I help my colleagues reflect</li>
  </ul>
  <div class="leaves" role="img" aria-label="Blue olive branch leaves"></div>
  <p class="brand-name">BLT</p>
  <p class="copyright">Copyright© 2026 BLT</p>
</section>

<section class="slide slide--step3b">
  <svg class="scenery" aria-hidden="true"><use href="#hills"/></svg>
  <div class="tree tree--left" role="img" aria-label="Faint tree silhouette"></div>
  <div class="tree tree--right" role="img" aria-label="Faint tree silhouette"></div>
  <h2 class="slide-title">Step 3B : Learning Journey</h2>
  <div class="stage-card detail-card">
    <div class="stage-badge">03</div>
    <p class="stage-name">The focus<br>is on “I”</p>
    <div class="doves" role="img" aria-label="One blue dove with two grey doves"></div>
  </div>
  <ul class="points points--snug">
    <li>I move to position the child as the owner of their own learning</li>
    <li>I give up control so the child can gain control</li>
    <li>The child becomes an architect in their curriculum</li>
    <li>The child becomes a collaborator in the how</li>
    <li>I am more a learner than a teacher</li>
    <li>I am a master of pedagogies</li>
    <li>I reflect on my practice through the eyes of children</li>
  </ul>
  <div class="leaves" role="img" aria-label="Blue olive branch leaves"></div>
  <p class="brand-name">BLT</p>
  <p class="copyright">Copyright© 2026 BLT</p>
</section>

<section class="slide slide--step4">
  <svg class="scenery" aria-hidden="true"><use href="#hills"/></svg>
  <div class="tree tree--left" role="img" aria-label="Faint tree silhouette"></div>
  <div class="tree tree--right" role="img" aria-label="Faint tree silhouette"></div>
  <h2 class="slide-title">Step 4 : Learning Journey</h2>
  <div class="stage-card detail-card">
    <div class="stage-badge">02</div>
    <p class="stage-name">Becoming part of the Christian Professional Learning Community</p>
    <div class="doves" role="img" aria-label="Three blue doves in flight"></div>
  </div>
  <ul class="points points--snug">
    <li>I am comfortable both in making the child owner and in taking on leadership roles with colleagues</li>
    <li>Children come to and stay at the school because I am there</li>
    <li>I want and work to ensure that every child to succeed</li>
    <li>I want and work to ensure that every one of my colleagues to succeed</li>
    <li>I am a master of several pedagogies</li>
    <li>I am a master of metacognition</li>
    <li>I see myself as a learner</li>
    <li>I reflect on my practice with my children / teens</li>
  </ul>
  <div class="leaves" role="img" aria-label="Blue olive branch leaves"></div>
  <p class="brand-name">BLT</p>
  <p class="copyright">Copyright© 2026 BLT</p>
</section>

</body>
</html>
```